Silver Bloom Marisol's Cleaning Service Business Cards Project

A business card with all contact details with logo design on there (already have a logo) eye catching Logo and contact info on one side, full logo on the back, must target upper class residential and corporate companies, fitness companies, still keep it on the feminine side of things , must look elegant

Target Market(s)

Upper class homes and corporate companies

Industry/Entity Type

Cleaning Service

Contact Information for Business Card

Name: Marisol Venturo
Position: Director
ABN: 47193802564
Email: marisolssilvercleaning@fernmail.test
Number: 0417968341

Font styles to use
Decorative

Colors

Designer to choose colors to be used in the design.

Requirements
Must have
• Available Sydney Wide, contact info and logo on one side, full logo on the back
Nice to have
• Professional appearance
Should not have
• Cheap advert looking stuff

```html
<!DOCTYPE html>
<html lang="en">
<head>
<meta charset="utf-8">
<title>Silver Bloom – Business Cards</title>
<link rel="stylesheet" href="https://fonts.googleapis.com/css2?family=Noto+Serif:wght@400;700&family=Roboto+Slab:wght@400;500&family=Josefin+Sans:wght@400&family=Roboto:wght@400;500&display=swap">
<style>
  :root {
    --stage: #3a3b3f;
    --navy: #2d3240;
    --teal: #3fe0d0;
    --teal-deep: #1aa8b0;
    --ink: #2a2d34;
    --paper: #ffffff;
    --muted: #c9ccd3;
  }
  * { box-sizing: border-box; margin: 0; padding: 0; }
  html, body { width: 1200px; height: 1000px; overflow: hidden; }
  body { background: var(--stage); position: relative; font-family: "Roboto", sans-serif; }

  .card { position: absolute; border-radius: 26px; overflow: hidden; }

  /* Back side */
  .card-back { left: 330px; top: 60px; width: 760px; height: 430px; background: var(--navy); }
  .card-back .logo-block { position: absolute; left: 0; right: 0; top: 70px; text-align: center; }
  .ornament { display: block; margin: 0 auto; border-radius: 60px; }
  .card-back .ornament { width: 380px; height: 120px;
    background: radial-gradient(ellipse at center, rgba(63,224,208,.35), rgba(63,224,208,.08) 70%, transparent); }
  .brand-name { font-family: "Noto Serif", serif; font-weight: 700; letter-spacing: 2px; text-transform: uppercase; }
  .card-back .brand-name { color: var(--teal); font-size: 42px; margin-top: 10px; }
  .tagline { font-family: "Josefin Sans", sans-serif; text-transform: uppercase; letter-spacing: 5px; }
  .card-back .tagline { color: var(--muted); font-size: 17px; margin-top: 6px; }

  /* Front side */
  .card-front { left: 110px; top: 410px; width: 820px; height: 460px; background: var(--paper); }
  .side-band { position: absolute; left: 0; top: 0; bottom: 0; width: 34px; background: var(--navy); }
  .side-rule { position: absolute; left: 34px; top: 0; bottom: 0; width: 8px; background: var(--teal); }
  .front-logo { position: absolute; left: 80px; top: 40px; width: 380px; text-align: center; }
  .card-front .ornament { width: 300px; height: 110px;
    background: radial-gradient(ellipse at center, rgba(42,45,52,.28), rgba(42,45,52,.06) 70%, transparent); }
  .card-front .brand-name { color: var(--ink); font-size: 34px; margin-top: 8px; }
  .card-front .tagline { color: var(--ink); font-size: 14px; margin-top: 4px; }

  .person { position: absolute; left: 80px; top: 262px; }
  .person-name { font-family: "Roboto Slab", serif; font-size: 30px; color: var(--ink); }
  .person-role { font-family: "Roboto Slab", serif; font-size: 20px; color: var(--teal-deep); }

  .contact { position: absolute; left: 80px; top: 350px; font-size: 17px; color: var(--ink); font-weight: 500; }
  .contact-row { display: flex; align-items: center; gap: 8px; height: 24px; }
  .contact-email { position: absolute; left: 300px; top: 374px; font-size: 17px; font-weight: 500; color: var(--ink); display: flex; align-items: center; gap: 8px; }
  .icon { width: 16px; height: 16px; fill: var(--teal-deep); }
  .footer-rule { position: absolute; left: 80px; right: 60px; top: 410px; height: 2px; background: var(--teal-deep); }
</style>
</head>
<body>
  <section class="card card-back" aria-label="Card back">
    <div class="logo-block">
      <div class="ornament" role="img" aria-label="Floral flourish ornament in teal"></div>
      <div class="brand-name">Silver Bloom</div>
      <div class="tagline">Marisol's Cleaning Services</div>
    </div>
  </section>

  <section class="card card-front" aria-label="Card front">
    <div class="side-band"></div>
    <div class="side-rule"></div>
    <div class="front-logo">
      <div class="ornament" role="img" aria-label="Floral flourish ornament in charcoal"></div>
      <div class="brand-name">Silver Bloom</div>
      <div class="tagline">Marisol's Cleaning Services</div>
    </div>
    <div class="person">
      <div class="person-name">Marisol Venturo</div>
      <div class="person-role">Director</div>
    </div>
    <div class="contact">
      <div class="contact-row">ABN: 47193802564</div>
      <div class="contact-row">
        <svg class="icon" viewBox="0 0 24 24" aria-hidden="true"><path d="M6.6 10.8a15 15 0 0 0 6.6 6.6l2.2-2.2a1 1 0 0 1 1-.25 11.4 11.4 0 0 0 3.6.57 1 1 0 0 1 1 1V20a1 1 0 0 1-1 1A17 17 0 0 1 3 4a1 1 0 0 1 1-1h3.5a1 1 0 0 1 1 1c0 1.25.2 2.45.57 3.6a1 1 0 0 1-.25 1z"/></svg>
        0417968341
      </div>
    </div>
    <div class="contact-email">
      <svg class="icon" viewBox="0 0 24 24" aria-hidden="true"><path d="M3 5h18a1 1 0 0 1 1 1v12a1 1 0 0 1-1 1H3a1 1 0 0 1-1-1V6a1 1 0 0 1 1-1zm9 7 8-5H4z"/></svg>
      marisolssilvercleaning@fernmail.test
    </div>
    <div class="footer-rule"></div>
  </section>
</body>
</html>
```